Playgrounds Unite Sponsorship Brochure

We need a 4 page sponsorship booklet designed for Playgrounds Unite. Playgrounds Unite is a scheme that brings top GB athletes into primary schools to encourage children to lead a healthy life and raise much needed funds for schools to buy new sports equipment. We would like to see designs that are eye catching, colourful and would appeal to children. I have attached the Kindly Lanterns Fundraising Pack (FULL PACK) for design ideas and a Word Document containing potential content (Sponsorship Form - Generic.docx) . I have also attached our brand guidelines and colour palette (Brand Guidelines PPT). WE would like to see pictures of our events and athletes to help bring the sponsorship form to life. I have attached some examples but please feel free to ask for more.

Target Market(s)

Children/Parents and Families/Friends

Requirements
Must have
• 4 pages
• Be a booklet
• Have a sponsorship form on the front
• Be eye catching
• Be colourful

```html
<!DOCTYPE html>
<html lang="en">
<head>
<meta charset="utf-8">
<title>Playgrounds Unite Sponsorship Booklet</title>
<link href="https://fonts.googleapis.com/css2?family=Lato:wght@400;700;900&family=Caveat:wght@600&display=swap" rel="stylesheet">
<style>
:root{
  --sky:#9cc9ec; --white:#fff; --ink:#333; --blue:#2a8fd0;
  --orange:#f5a23a; --orange-deep:#ef7f22; --red:#e0213a; --yellow:#f6e23a;
  --green:#8cc63f; --green-deep:#5aa73a; --purple:#b9578f; --purple-light:#d27cae;
  --teal:#2fa3de; --bg:#eceef0; --pill:#f8c79a;
}
*{margin:0;padding:0;box-sizing:border-box}
html,body{width:874px;height:1200px;overflow:hidden;background:var(--bg);font-family:Lato,Arial,sans-serif;color:var(--ink)}
.canvas{position:relative;width:874px;height:1200px}
.page{position:absolute;width:372px;height:526px;overflow:hidden;background:linear-gradient(180deg,var(--sky) 0%,#b3d8f3 100%)}
.abs,.ph{position:absolute}
.ribbon{position:absolute;height:24px;color:#fff;font-size:13px;line-height:24px;padding-left:22px;letter-spacing:-.2px}
.ribbon::after{content:"";position:absolute;right:-22px;top:6px;width:30px;height:22px;background:inherit;filter:brightness(.85);clip-path:polygon(0 0,100% 0,70% 50%,100% 100%,0 100%);z-index:-1}
.cloud{position:absolute;background:#fff;border-radius:50%}
.label{font-size:7px;color:#fff}
.pill{position:absolute;height:15px;border-radius:8px;background:var(--pill);color:#fff;font-size:6px;line-height:15px;padding-left:8px}
.seal{position:absolute;width:44px;height:44px;border-radius:50%;background:var(--red);border:2px solid #fff;color:#fff;font-size:7px;font-weight:700;text-align:center;line-height:8px;padding-top:12px;box-shadow:0 1px 3px rgba(0,0,0,.25)}
.photo{position:absolute;border:3px solid #fff;box-shadow:0 2px 4px rgba(0,0,0,.25)}
.brand{font-weight:700;color:#222;letter-spacing:-.5px;white-space:nowrap}
.dot{display:inline-block;border-radius:50%;vertical-align:middle}
.step{position:absolute;width:56px;height:56px;border-radius:50%;border:5px solid var(--red);background:#fff;color:var(--blue);font-size:18px;font-weight:700;text-align:center;line-height:46px;box-shadow:0 2px 3px rgba(0,0,0,.2)}
.step-title{position:absolute;left:92px;font-size:9px;font-weight:900;color:var(--red)}
.step-text{position:absolute;left:92px;width:180px;font-size:8px;line-height:11px}
.h-blue{color:var(--blue);font-size:11px}
.body{font-size:7.5px;line-height:10.5px;color:#333}
.cost{position:absolute;left:22px;width:336px;height:26px;color:#fff;font-size:9.5px;line-height:26px;padding-left:10px}
.cost span{position:absolute;right:0;top:0;width:112px;height:26px;text-align:center;font-size:13px}
</style>
</head>
<body>
<div class="canvas">

<!-- Spread one, left: quiz corner -->
<section class="page" style="left:80px;top:52px">
  <div class="ribbon" style="left:0;top:20px;width:150px;background:var(--yellow);color:var(--red);z-index:2">QUIZ CORNER</div>
  <div class="ph" role="img" aria-label="Elephant shaped maze puzzle" style="left:22px;top:78px;width:170px;height:180px;border-radius:40% 45% 30% 30%;background:rgba(255,255,255,.25);border:2px solid rgba(255,255,255,.7)"></div>
  <div class="abs label" style="left:38px;top:286px">Maze</div>
  <div class="ph" role="img" aria-label="Colouring outline of a running boy" style="left:200px;top:10px;width:110px;height:160px;border-radius:40%;background:rgba(255,255,255,.55)"></div>
  <div class="abs label" style="left:292px;top:58px">Colouring</div>
  <div class="abs label" style="left:250px;top:182px;transform:rotate(15deg)">Spot the Difference</div>
  <div class="ph" role="img" aria-label="Spot the difference cartoon puzzle" style="left:186px;top:200px;width:140px;height:140px;border-radius:18px;background:linear-gradient(135deg,#e9c35a,#a3753a);transform:rotate(12deg)"></div>
  <div class="cloud" style="left:-30px;top:340px;width:200px;height:120px"></div>
  <div class="cloud" style="left:120px;top:320px;width:180px;height:130px"></div>
  <div class="cloud" style="left:260px;top:345px;width:170px;height:110px"></div>
  <div class="ph" role="img" aria-label="Four smiling children lying on the grass" style="left:0;top:370px;width:372px;height:156px;background:linear-gradient(180deg,#f2c6a8 0%,#e4584a 55%,#7cbf3d 100%)"></div>
</section>

<!-- Spread one, right: sponsorship form -->
<section class="page" style="left:452px;top:52px">
  <div class="abs" style="left:22px;top:14px;width:330px;display:flex;gap:18px;font-size:5.5px;color:#fff">
    <div style="flex:1;border-bottom:1px dotted #fff;padding-bottom:10px">MY NAME:</div>
    <div style="flex:1;border-bottom:1px dotted #fff;padding-bottom:10px">MY CLASS:</div>
    <div style="flex:1;border-bottom:1px dotted #fff;padding-bottom:10px">I'VE RAISED: £</div>
  </div>
  <div class="abs" style="left:28px;top:68px;width:318px;height:96px;border-radius:12px;background:var(--orange);color:#fff;font-size:6.8px;line-height:9px;text-align:center;padding:24px 12px 0">
    I'm going to be taking part in a fun fitness circuit alongside a top GB athlete.
    <span style="display:block;margin-top:5px">Please sponsor me to help raise money for new sports equipment for my school and to help support GB athletes to compete for our country and inspire the next generation.</span>
    <span style="display:block;margin-top:5px">As a thank you, if I meet these milestones, I'll receive the following prizes:</span>
  </div>
  <div class="abs" style="left:66px;top:54px;width:240px;height:26px;background:var(--red);color:#fff;font-size:15px;text-align:center;line-height:26px">MY SPONSORSHIP FORM</div>
  <div class="photo" role="img" aria-label="Sprinter on the track" style="left:24px;top:156px;width:106px;height:62px;background:linear-gradient(135deg,#3f7a3a,#b4563a);transform:rotate(-3deg)"></div>
  <div class="photo" role="img" aria-label="Gymnast on the rings" style="left:142px;top:146px;width:106px;height:64px;background:linear-gradient(135deg,#222,#7a2030)"></div>
  <div class="photo" role="img" aria-label="Athlete in a crouched pose outdoors" style="left:256px;top:154px;width:106px;height:62px;background:linear-gradient(135deg,#5d8a3a,#c9a37c);transform:rotate(3deg)"></div>
  <div class="seal" style="left:88px;top:180px">RAISE<br>OVER £5</div>
  <div class="seal" style="left:168px;top:186px">RAISE<br>OVER £15</div>
  <div class="seal" style="left:238px;top:180px">RAISE<br>OVER £15</div>
  <div class="pill" style="left:28px;top:236px;width:96px">NAME</div>
  <div class="pill" style="left:134px;top:236px;width:96px">AMOUNT SPONSORED (£)</div>
  <div class="pill" style="left:250px;top:236px;width:96px">PAID? (PLEASE TICK)</div>
  <div class="abs" style="left:28px;top:258px;width:318px;height:70px;background:repeating-linear-gradient(180deg,#cfe4f7 0 11px,#a8cdee 11px 12px)"></div>
  <div class="cloud" style="left:-30px;top:336px;width:180px;height:120px"></div>
  <div class="cloud" style="left:90px;top:306px;width:220px;height:150px"></div>
  <div class="cloud" style="left:250px;top:336px;width:170px;height:120px"></div>
  <div class="abs brand" style="left:64px;top:400px;font-size:20px"><span class="dot" style="width:24px;height:24px;background:var(--red);margin-right:10px"></span>PLAYGROUNDS UNITE</div>
  <div class="abs" style="left:0;top:440px;width:372px;height:86px;background:var(--green);border-radius:50% 50% 0 0/18px 18px 0 0;color:#fff;text-align:center;font-size:8.5px;line-height:12px;padding-top:14px">
    To find out more about Playgrounds Unite and how we fund the scheme,<br>visit: <b>www.PlaygroundsUnite.org/funding-for-schools/</b>
    <div style="display:flex;justify-content:space-around;align-items:center;margin-top:12px;padding:0 20px">
      <span style="font-size:9px">CLUBHOUSE CIRCLE</span>
      <span style="font-size:13px;font-weight:900">SUNBEAM SUBS</span>
      <span style="display:inline-block;width:56px;height:24px;background:#fff"></span>
    </div>
  </div>
</section>

<!-- Spread two, left: the event -->
<section class="page" style="left:80px;top:622px;background:linear-gradient(180deg,#fff 0%,#fff 30%,#b6d8f2 65%,#a6cff0 100%)">
  <div class="ribbon" style="left:0;top:20px;width:150px;background:var(--orange-deep);z-index:2">THE EVENT</div>
  <div class="abs" style="left:22px;top:60px;width:336px">
    <div class="h-blue">THE EVENT DAY</div>
    <p class="body" style="margin-top:3px">I'll complete the fitness circuit alongside the athlete, listen to an inspirational assembly and ask any questions I may have.</p>
    <div class="h-blue" style="margin-top:12px">THE DVD ASSEMBLY</div>
    <p class="body" style="margin-top:3px">I'll watch a DVD in assembly to reveal which GB athlete is visiting my school and what sport they compete in. I'll also learn the exercises that I'll be doing with the athlete on the day.</p>
  </div>
  <div class="abs" style="left:22px;top:152px;width:336px;height:76px;border-radius:10px;background:var(--orange);color:#fff;text-align:center;padding-top:10px">
    <div style="font-size:11px">PRACTICE</div>
    <div style="font-size:7px;margin-top:3px">I'll practice the 4 exercises before the event so I can show the athlete what I've learnt.</div>
  </div>
  <div class="photo" role="img" aria-label="Children exercising in a school hall" style="left:20px;top:208px;width:96px;height:70px;background:linear-gradient(135deg,#c9b36a,#4b8ac4);transform:rotate(-6deg)"></div>
  <div class="photo" role="img" aria-label="Children stretching together" style="left:104px;top:206px;width:92px;height:70px;background:linear-gradient(135deg,#6b6b4a,#d7a27a);transform:rotate(6deg)"></div>
  <div class="photo" role="img" aria-label="Group of pupils in coloured bibs" style="left:186px;top:210px;width:94px;height:70px;background:linear-gradient(135deg,#e6e07a,#c9473a);transform:rotate(-5deg)"></div>
  <div class="photo" role="img" aria-label="Boy holding a trophy" style="left:270px;top:206px;width:92px;height:70px;background:linear-gradient(135deg,#3c3a3a,#e6b43a);transform:rotate(6deg)"></div>
  <div class="ribbon" style="left:0;top:306px;width:150px;background:var(--yellow);z-index:2">THE EXERCISES</div>
  <div class="ph" role="img" aria-label="Outline figures doing four exercises" style="left:160px;top:300px;width:196px;height:50px;border-radius:8px;background:rgba(255,255,255,.45)"></div>
  <div class="abs body" style="left:22px;top:362px">I will complete as many of the following exercises as I can in 1 minute intervals</div>
  <div class="abs" style="left:22px;top:378px;width:130px;height:22px;background:var(--purple);color:#fff;font-size:12px;line-height:22px;padding-left:12px">After the Event</div>
  <div class="abs" style="left:22px;top:400px;width:336px;height:34px;background:var(--purple-light);color:#fff;font-size:7px;line-height:10px;padding:7px 12px">I'll have one week to collect up my sponsorship money and then I will need to return the front two pages of this form to the school office.</div>
  <div class="cost" style="top:436px;background:var(--teal)">Could buy my school 15 footballs<span style="background:#1d86c7">£100</span></div>
  <div class="cost" style="top:462px;background:#4cbde8">Could buy my school 2 basketball hoops<span style="background:var(--teal)">£250</span></div>
  <div class="cost" style="top:488px;background:var(--green);font-size:9px">Could buy my school a gym mat trolley &amp; 5 gym mats<span style="background:var(--green-deep)">£500</span></div>
</section>

<!-- Spread two, right: get online -->
<section class="page" style="left:452px;top:622px">
  <div class="ribbon" style="left:18px;top:16px;width:132px;background:var(--teal);z-index:2">GET ONLINE!</div>
  <div class="abs" style="left:312px;top:10px;width:54px;height:60px;background:#f3efe4"></div>
  <div class="abs" style="left:18px;top:38px;width:336px;height:88px;border-radius:0 0 12px 12px;background:var(--green);color:#fff;font-size:11.5px;line-height:18px;text-align:center;padding-top:24px">Find out more about your event and the Athlete visiting<br>your schools at <b>www.PlaygroundsUnite.org/MyEvent</b></div>
  <div class="ph" role="img" aria-label="Girl jumping in the air" style="left:286px;top:118px;width:86px;height:240px;border-radius:40px;background:linear-gradient(180deg,#7a4a2a,#2a9bd6 40%,#27364e 75%)"></div>
  <div class="step" style="left:26px;top:154px">1.</div>
  <div class="step-title" style="top:166px">SET UP AN ONLINE FUNDRAISING PAGE</div>
  <div class="step-text" style="top:178px">(takes 90 seconds) Simply visit<br><b>www.playgroundsunite.org/sponsormychild</b></div>
  <div class="step" style="left:26px;top:218px;border-color:var(--orange-deep)">2.</div>
  <div class="step-title" style="top:230px">MAKE THE 1ST DONATION</div>
  <div class="step-text" style="top:242px">The best way to encourage others to support your child is to be the first to sponsor them. The amount is less important than the act!</div>
  <div class="step" style="left:26px;top:284px;border-color:var(--orange)">3.</div>
  <div class="step-title" style="top:298px">INVITE OTHERS</div>
  <div class="step-text" style="top:310px">Share your child's fundraising page with friends and family to get the donations rolling in.</div>
  <div class="cloud" style="left:-40px;top:384px;width:200px;height:130px"></div>
  <div class="cloud" style="left:70px;top:350px;width:240px;height:160px"></div>
  <div class="cloud" style="left:250px;top:388px;width:180px;height:120px"></div>
  <div class="abs" style="left:132px;top:364px;font-family:Caveat,cursive;font-size:19px;color:var(--red);transform:rotate(5deg);white-space:nowrap">1,500,000 kids inspired</div>
  <div class="abs brand" style="left:82px;top:396px;font-size:17px"><span class="dot" style="width:22px;height:22px;background:var(--red);margin-right:8px"></span>PLAYGROUNDS UNITE</div>
  <div class="abs" style="left:114px;top:418px;font-size:7px;letter-spacing:1.2px">GB ATHLETES WHO INSPIRE KIDS</div>
  <div class="abs" style="left:114px;top:434px;font-size:5.5px;line-height:7px;display:flex;gap:14px">
    <span>Follow us on Chirper<br>@playunite</span><span>Like us on Friendbook<br>@playgroundsunite</span>
  </div>
  <div class="abs" style="left:0;top:462px;width:372px;height:64px;background:var(--green);border-radius:50% 50% 0 0/14px 14px 0 0;text-align:center;color:#fff;padding-top:10px">
    <div style="font-size:10px">Subscribe to our news! www.playgroundsunite.org</div>
    <div style="font-size:7px;margin-top:2px">We'd love to hear from you – post us your pictures and comments on social media</div>
    <div style="font-size:7px;color:var(--red);margin-top:3px;line-height:9px">To find out more about Playgrounds Unite and how we fund the scheme,<br>visit: www.PlaygroundsUnite.org/funding-for-schools/</div>
  </div>
</section>

</div>
</body>
</html>
```